Real Estate Company Needs Business Card Designed

We need a business card design for a new real estate company based in Marlow Bay, CA (Harbor District). We plan to improve the residential real estate industry by using technology to improve customer experience. We would like to see designs that use a black background. The final design should communicate sophistication and customer service, as well as stability and technology.

Industry/Entity Type

Real Estate

Requirements
Must have
• Black background

```html
<!DOCTYPE html>
<html lang="en">
<head>
<meta charset="utf-8">
<title>Kestrine Business Card</title>
<link rel="stylesheet" href="https://fonts.googleapis.com/css2?family=Crimson+Text:wght@400;600&display=swap">
<style>
  :root {
    --backdrop: #d9d9d7;
    --card-black: #000000;
    --ink-white: #ffffff;
    --ink-soft: #e6e6e6;
    --accent-red: #e21d2f;
    --brand-blue: #8fb0e8;
  }
  * { margin: 0; padding: 0; box-sizing: border-box; }
  html, body {
    width: 1200px; height: 926px; overflow: hidden;
    background: var(--backdrop);
    font-family: "Crimson Text", Georgia, serif;
  }
  .canvas { position: relative; width: 1200px; height: 926px; }
  .card {
    position: absolute; left: 250px; width: 700px; height: 400px;
    background: var(--card-black); overflow: hidden;
    box-shadow: 0 6px 18px rgba(0,0,0,0.25);
  }
  .card--front { top: 42px; }
  .card--back { top: 484px; }

  /* Front face */
  .brand-name {
    position: absolute; color: var(--brand-blue);
    font-weight: 400; letter-spacing: 0.02em; line-height: 1;
  }
  .card--front .brand-name { left: 40px; top: 64px; font-size: 38px; }
  .divider { position: absolute; left: 262px; width: 2px; background: var(--ink-white); }
  .divider--top { top: 0; height: 56px; }
  .divider--middle { top: 104px; height: 160px; }
  .divider--bottom { top: 300px; height: 56px; }
  .company-name {
    position: absolute; left: 288px; top: 62px;
    color: var(--ink-white); font-size: 27px; font-weight: 400;
  }
  .person {
    position: absolute; right: 458px; top: 196px; text-align: right;
    color: var(--ink-white);
  }
  .person__name { font-size: 25px; line-height: 1; letter-spacing: 0.01em; }
  .person__title { font-size: 11px; letter-spacing: 0.06em; margin-top: 4px; }
  .contact {
    position: absolute; left: 290px; top: 210px;
    color: var(--ink-soft); font-size: 14.5px; line-height: 1.3;
    letter-spacing: 0.02em; font-style: normal;
  }
  .red-band {
    position: absolute; left: 0; right: 0; bottom: 0; height: 44px;
    background: var(--accent-red);
  }

  /* Back face */
  .back-lockup { position: absolute; left: 0; right: 0; top: 148px; text-align: center; }
  .card--back .brand-name { position: static; display: block; font-size: 68px; }
  .full-name {
    display: block; margin-top: 16px; color: var(--ink-white);
    font-size: 11px; font-weight: 600; letter-spacing: 0.28em;
  }
</style>
</head>
<body>
<main class="canvas">
  <section class="card card--front" aria-label="Business card front">
    <div class="brand-name">KESTRINE</div>
    <span class="divider divider--top"></span>
    <span class="divider divider--middle"></span>
    <span class="divider divider--bottom"></span>
    <h1 class="company-name">Company Full name</h1>
    <div class="person">
      <div class="person__name">PERSON NAME</div>
      <div class="person__title">PERSON TITLE</div>
    </div>
    <address class="contact">
      428 Orchard Ln., Marlow Bay, CA (Harbor District)<br>
      o: 555.018.2746 &nbsp;|&nbsp; c: 555.018.3391<br>
      e: hello@kestrine.com
    </address>
    <div class="red-band"></div>
  </section>

  <section class="card card--back" aria-label="Business card back">
    <div class="back-lockup">
      <span class="brand-name">KESTRINE</span>
      <span class="full-name">FULL NAME OF KESTRINE</span>
    </div>
  </section>
</main>
</body>
</html>
```